Bright Pelvic Health Business Card

Need a business card for a surgical practice called Bright Pelvic Health. We have recently selected a logo (attached). The business card will need to have two formats:
1) One with the logo/physician name/ contact info on the front and location information on the back.
2) One in "appointment reminder card" style with the logo/ contact info/ date/ time on the front and the location information on the back.

The front side should include the following information:
- Logo
- Ravi K. Desai, MD FACOG
- phone: 469-555-0182
- fax: 1-469-555-0147
- email: admin@brightpelvic.example
- website: www.brightpelvichealth.example

The back side should have the office locations listed:
4812 Quarry Bend Dr, Plano, TX 75093
3650 Wrenfield Rd, Plano, TX 75025
2245 Brambleton Ln, Irving, TX 75038
915 S Garnet Ave B314, Dallas, TX 75201
1836 Tillman Pkwy, Grand Prairie, TX 75051
6417 Dorrance Way Dr, San Antonio, TX 78240
5920 Kessler Rd, Pasadena, TX 77504

Target Market(s)

1. Other physicians who might refer patients
2. Female patients

Industry/Entity Type

Business

Font styles to use
Other font styles liked:
• Tahoma for lettering

Requirements
Must have
• As per the instructions
Should not have
• No other images needed -- please try to keep font consistent with logo design. Can use Tahoma as the font for lettering.

```html
<!DOCTYPE html>
<html lang="en">
<head>
<meta charset="utf-8">
<title>Bright Pelvic Health – Business Card</title>
<link rel="stylesheet" href="https://fonts.googleapis.com/css2?family=Open+Sans:wght@400;600&display=swap">
<style>
  :root {
    --page-bg: #e4e4e4;
    --card-bg: #ffffff;
    --brand-blue: #2a4f9e;
    --accent-red: #e03b3b;
    --ink: #1b1b1b;
    --icon-bg: #2a4f9e;
    --icon-fg: #ffffff;
    --card-shadow: rgba(0, 0, 0, 0.18);
  }
  * { box-sizing: border-box; margin: 0; padding: 0; }
  html, body {
    width: 1170px; height: 1200px; overflow: hidden;
    background: var(--page-bg);
    font-family: "Open Sans", Tahoma, Verdana, sans-serif;
    color: var(--ink);
  }
  .sheet {
    width: 1170px; height: 1200px;
    display: flex; flex-direction: column; align-items: center;
    justify-content: center; gap: 40px;
  }
  .card {
    position: relative;
    width: 900px; height: 540px;
    background: var(--card-bg);
    box-shadow: 0 2px 10px var(--card-shadow);
  }

  /* Front */
  .brand {
    position: absolute; left: 0; right: 0;
    display: flex; align-items: center; justify-content: center; gap: 16px;
    color: var(--brand-blue); font-weight: 600; white-space: nowrap;
  }
  .brand-dot { border-radius: 50%; background: var(--accent-red); flex: none; }
  .card-front .brand { top: 200px; font-size: 58px; }
  .card-front .brand-dot { width: 26px; height: 26px; }

  .physician {
    position: absolute; left: 0; right: 0; top: 318px;
    text-align: center;
  }
  .physician-name { font-size: 38px; font-weight: 400; line-height: 1.1; }
  .physician-credentials { font-size: 19px; letter-spacing: 0.5px; margin-top: 2px; }

  .contact {
    position: absolute; top: 440px;
    list-style: none; display: flex; flex-direction: column; gap: 12px;
  }
  .contact-left { left: 96px; }
  .contact-right { left: 500px; }
  .contact li { display: flex; align-items: center; gap: 12px; font-size: 23px; }
  .contact-icon { width: 30px; height: 30px; flex: none; }

  /* Back */
  .card-back .brand { top: 78px; font-size: 24px; gap: 8px; }
  .card-back .brand-dot { width: 12px; height: 12px; }
  .locations-title {
    position: absolute; left: 0; right: 0; top: 152px;
    text-align: center; font-size: 44px; font-weight: 400;
  }
  .locations {
    position: absolute; left: 60px; top: 242px;
    list-style: none;
  }
  .locations li {
    display: flex; align-items: center; gap: 8px;
    font-size: 27px; line-height: 36px; white-space: nowrap;
  }
  .locations li::before {
    content: ""; width: 18px; height: 18px; border-radius: 50%;
    background: var(--brand-blue); flex: none;
  }
  .locations li:nth-child(2) { margin-left: 28px; }
  .locations li:nth-child(3) { margin-left: 56px; }
  .locations li:nth-child(4) { margin-left: 84px; }
  .locations li:nth-child(5) { margin-left: 112px; }
  .locations li:nth-child(6) { margin-left: 140px; }
  .locations li:nth-child(7) { margin-left: 168px; }
</style>
</head>
<body>
<main class="sheet">

  <section class="card card-front" aria-label="Business card front">
    <div class="brand"><span class="brand-dot"></span><span class="brand-name">Bright Pelvic Health</span></div>

    <div class="physician">
      <p class="physician-name">Ravi K. Desai</p>
      <p class="physician-credentials">MD FACOG</p>
    </div>

    <ul class="contact contact-left">
      <li>
        <svg class="contact-icon" viewBox="0 0 30 30" aria-label="Phone">
          <circle cx="15" cy="15" r="15" fill="var(--icon-bg)"/>
          <rect x="10.5" y="6.5" width="9" height="17" rx="1.5" fill="none" stroke="var(--icon-fg)" stroke-width="1.8"/>
          <rect x="12.5" y="9" width="5" height="6" fill="var(--icon-fg)"/>
          <circle cx="15" cy="19.5" r="1.3" fill="var(--icon-fg)"/>
        </svg>
        <span>469-555-0182</span>
      </li>
      <li>
        <svg class="contact-icon" viewBox="0 0 30 30" aria-label="Fax">
          <circle cx="15" cy="15" r="15" fill="var(--icon-bg)"/>
          <rect x="10" y="7" width="10" height="6" fill="var(--icon-fg)"/>
          <rect x="7" y="12" width="16" height="8" rx="1.5" fill="var(--icon-fg)"/>
          <rect x="10" y="17" width="10" height="6" fill="var(--icon-fg)" stroke="var(--icon-bg)" stroke-width="1.2"/>
        </svg>
        <span>1-469-555-0147</span>
      </li>
    </ul>

    <ul class="contact contact-right">
      <li>
        <svg class="contact-icon" viewBox="0 0 30 30" aria-label="Email">
          <circle cx="15" cy="15" r="15" fill="var(--icon-bg)"/>
          <rect x="7.5" y="9.5" width="15" height="11" fill="var(--icon-fg)"/>
          <path d="M7.5 9.5 L15 16 L22.5 9.5" fill="none" stroke="var(--icon-bg)" stroke-width="1.5"/>
        </svg>
        <span>admin@brightpelvic.example</span>
      </li>
      <li>
        <svg class="contact-icon" viewBox="0 0 30 30" aria-label="Website">
          <circle cx="15" cy="15" r="15" fill="var(--icon-bg)"/>
          <g fill="none" stroke="var(--icon-fg)" stroke-width="1.5">
            <circle cx="15" cy="15" r="8"/>
            <ellipse cx="15" cy="15" rx="3.5" ry="8"/>
            <line x1="7" y1="15" x2="23" y2="15"/>
            <path d="M8.5 11 H21.5 M8.5 19 H21.5"/>
          </g>
        </svg>
        <span>www.brightpelvichealth.example</span>
      </li>
    </ul>
  </section>

  <section class="card card-back" aria-label="Business card back">
    <div class="brand"><span class="brand-dot"></span><span class="brand-name">Bright Pelvic Health</span></div>
    <h2 class="locations-title">Our office locations</h2>
    <ul class="locations">
      <li>4812 Quarry Bend Dr, Plano, TX 75093</li>
      <li>3650 Wrenfield Rd, Plano, TX 75025</li>
      <li>2245 Brambleton Ln, Irving, TX 75038</li>
      <li>915 S Garnet Ave B314, Dallas, TX 75201</li>
      <li>1836 Tillman Pkwy, Grand Prairie, TX 75051</li>
      <li>6417 Dorrance Way Dr, San Antonio, TX 78240</li>
      <li>5920 Kessler Rd, Pasadena, TX 77504</li>
    </ul>
  </section>

</main>
</body>
</html>
```